Brochure required

Looking at getting business brochure designed for my solar sales company. i will require a range of products to be listed on the brochure I require a simple/ elegent / professional looking brochure.

I am happy to provide designer with all the required information that must go into the brochure. otherwise please visit www.velorquintade.com.au and view the products which i would like to allocate into the brochure aswell as our company logo and a little about me section

```html
<!DOCTYPE html>
<html lang="en">
<head>
<meta charset="utf-8">
<title>Velorquintade brochure</title>
<link rel="stylesheet" href="https://fonts.googleapis.com/css2?family=Lato:wght@400;700;900&display=swap">
<style>
:root{
  --bg:#e8e1dc;
  --paper:#ffffff;
  --teal:#1db48e;
  --teal-dark:#13987a;
  --blue:#1a86c2;
  --gold:#c4a22a;
  --ink:#2f3236;
  --muted:#5b6066;
  --rule:#d9dde0;
}
*{box-sizing:border-box;margin:0;padding:0}
html,body{width:768px;height:1200px;overflow:hidden;background:var(--bg)}
body{font-family:"Lato",sans-serif;color:var(--ink);position:relative}
.spread{position:absolute;left:24px;width:720px;height:509px;display:flex;box-shadow:0 6px 18px rgba(0,0,0,.12)}
.spread--cover{top:40px}
.spread--inside{top:609px}
.page{position:relative;width:360px;height:509px;background:var(--paper);overflow:hidden}
.page + .page{border-left:1px solid #eceff1}
.page svg.art{position:absolute;inset:0;width:360px;height:509px}

.brand{position:absolute;display:flex;align-items:center;gap:6px;font-weight:900;color:var(--ink)}
.brand__mark{width:14px;height:14px;background:var(--teal)}
.brand--front{left:40px;top:46px;font-size:19px}
.brand--back{left:176px;top:272px;font-size:15px}
.brand--back .brand__mark{width:11px;height:11px}

.headline{position:absolute;left:30px;top:80px;line-height:1.02}
.headline__lead{display:block;color:var(--blue);font-size:25px;font-weight:700}
.headline__tail{display:block;color:var(--ink);font-size:25px;font-weight:700;padding-left:50px}

.contact{position:absolute;left:176px;top:296px;width:170px}
.contact__call{color:var(--teal);font-size:10px;font-weight:700;letter-spacing:.5px}
.contact__phone{font-size:21px;font-weight:700;color:var(--ink);margin-top:2px}
.contact__row{display:flex;flex-direction:column;align-items:center;margin-top:8px;width:150px}
.contact__icon{width:14px;height:14px;border-radius:50%;background:var(--blue);display:flex;align-items:center;justify-content:center}
.contact__text{font-size:8px;color:var(--muted);margin-top:3px}

.intro{position:absolute;left:30px;top:26px;width:300px;font-size:7.5px;line-height:1.45;color:var(--muted)}
.product{position:absolute;width:200px}
.product__title{color:var(--blue);font-size:11px;font-weight:700;text-transform:uppercase;letter-spacing:.3px;margin-bottom:4px}
.product__body{font-size:7.2px;line-height:1.45;color:var(--muted);margin-bottom:4px}
.product__note{position:absolute;width:300px;font-size:7.2px;line-height:1.45;color:var(--muted)}
.photo-tile{position:absolute}

.ppa{position:absolute;left:24px;top:262px;width:310px}
.ppa .product__title{margin-bottom:4px}
.chart{position:absolute;left:40px;top:350px;width:290px;height:140px}
.chart text{font-family:"Lato",sans-serif}
</style>
</head>
<body>

<!-- Outer covers: back (left) and front (right) -->
<section class="spread spread--cover">
  <article class="page page--back">
    <svg class="art" viewBox="0 0 360 509" aria-hidden="false">
      <defs>
        <linearGradient id="installerPhoto" x1="0" y1="0" x2="0.3" y2="1">
          <stop offset="0" stop-color="#6f9fd1"/>
          <stop offset=".45" stop-color="#4b7ab8"/>
          <stop offset=".7" stop-color="#d9742f"/>
          <stop offset="1" stop-color="#2a3f6a"/>
        </linearGradient>
        <linearGradient id="backWave" x1="0" y1="0" x2="1" y2="0">
          <stop offset="0" stop-color="var(--teal)"/>
          <stop offset="1" stop-color="var(--blue)"/>
        </linearGradient>
      </defs>
      <path d="M160 40 A 132 132 0 0 1 140 265" fill="none" stroke="var(--gold)" stroke-width="7"/>
      <circle cx="70" cy="150" r="125" fill="url(#installerPhoto)" role="img" aria-label="Photo of an installer in a safety helmet fitting a solar panel on a roof"/>
      <path d="M0 470 C 120 430, 250 440, 360 400 L360 509 L0 509 Z" fill="url(#backWave)"/>
      <path d="M0 470 C 120 430, 250 440, 360 400" fill="none" stroke="#ffffff" stroke-width="4"/>
    </svg>
    <div class="brand brand--back"><span class="brand__mark"></span>Velorquintade</div>
    <div class="contact">
      <div class="contact__call">CALL US NOW</div>
      <div class="contact__phone">0400 555 218</div>
      <div class="contact__row">
        <span class="contact__icon"><svg width="8" height="6" viewBox="0 0 8 6"><rect x=".5" y=".5" width="7" height="5" fill="none" stroke="#fff" stroke-width="1"/><path d="M.5 .5 L4 3.5 L7.5 .5" fill="none" stroke="#fff" stroke-width="1"/></svg></span>
        <span class="contact__text">info@velorquintade.com.au</span>
      </div>
      <div class="contact__row">
        <span class="contact__icon"><svg width="8" height="8" viewBox="0 0 8 8"><circle cx="4" cy="4" r="3.3" fill="none" stroke="#fff" stroke-width="1"/><path d="M.7 4 H7.3 M4 .7 C2.5 2.5 2.5 5.5 4 7.3 M4 .7 C5.5 2.5 5.5 5.5 4 7.3" fill="none" stroke="#fff" stroke-width=".8"/></svg></span>
        <span class="contact__text">www.velorquintade.com.au</span>
      </div>
    </div>
  </article>

  <article class="page page--front">
    <svg class="art" viewBox="0 0 360 509">
      <defs>
        <linearGradient id="solarFieldPhoto" x1="0" y1="0" x2="0" y2="1">
          <stop offset="0" stop-color="#9cc3e6"/>
          <stop offset=".35" stop-color="#f3d9a6"/>
          <stop offset=".55" stop-color="#3a4f72"/>
          <stop offset=".8" stop-color="#4f7a3a"/>
          <stop offset="1" stop-color="#3d6a2a"/>
        </linearGradient>
      </defs>
      <path d="M95 212 C 200 210, 300 222, 360 242 L360 509 L150 509 C 108 440, 92 330, 95 212 Z" fill="var(--teal)"/>
      <circle cx="262" cy="395" r="131" fill="#ffffff"/>
      <circle cx="262" cy="395" r="124" fill="url(#solarFieldPhoto)" role="img" aria-label="Photo of solar panel rows in a grassy field under a setting sun"/>
    </svg>
    <div class="brand brand--front"><span class="brand__mark"></span>Velorquintade</div>
    <h1 class="headline">
      <span class="headline__lead">Energy solutions for a</span>
      <span class="headline__tail">changing world</span>
    </h1>
  </article>
</section>

<!-- Inside spread -->
<section class="spread spread--inside">
  <article class="page page--panels">
    <svg class="art" viewBox="0 0 360 509">
      <defs>
        <linearGradient id="rooftopPhoto" x1="0" y1="0" x2="1" y2="1">
          <stop offset="0" stop-color="#e9c98c"/>
          <stop offset=".35" stop-color="#5f7fa6"/>
          <stop offset=".7" stop-color="#35507a"/>
          <stop offset="1" stop-color="#4e7b36"/>
        </linearGradient>
      </defs>
      <path d="M0 345 C 120 315, 260 330, 360 380 L360 509 L0 509 Z" fill="var(--teal)"/>
      <path d="M0 356 C 120 328, 260 342, 360 392 L360 509 L0 509 Z" fill="#ffffff"/>
      <path d="M0 362 C 120 336, 260 350, 360 400 L360 509 L0 509 Z" fill="url(#rooftopPhoto)" role="img" aria-label="Photo of a large solar panel array at sunset"/>
    </svg>
    <p class="intro">Velorquintade has partnered with trusted solar makers to bring you quality panels and inverters. Each product is chosen for output, warranty and long life on Australian roofs.</p>

    <svg class="photo-tile" style="left:28px;top:96px" width="82" height="92" viewBox="0 0 82 92">
      <rect x="4" y="2" width="74" height="88" fill="#1f2b44" role="img" aria-label="Product shot of a 270W solar panel"/>
    </svg>
    <div class="product" style="left:122px;top:98px">
      <h2 class="product__title">Solvane 270W</h2>
      <p class="product__body">A durable module built for high output in heat, with strong ratings for wind and snow loads.</p>
    </div>
    <p class="product__note" style="left:30px;top:196px">This panel sets a steady standard for reliable home systems at a fair price.</p>

    <svg class="photo-tile" style="left:28px;top:222px" width="82" height="70" viewBox="0 0 82 70">
      <rect x="4" y="2" width="74" height="66" fill="#2c4a8c" role="img" aria-label="Product shot of a 300W monocrystalline solar panel"/>
    </svg>
    <div class="product" style="left:122px;top:226px">
      <h2 class="product__title">Solvane Hawk Perc 60M 300W</h2>
      <p class="product__body">A highly efficient mono panel from a tier one maker at an affordable price.</p>
    </div>
    <p class="product__note" style="left:30px;top:300px">Its split cell design lifts efficiency while keeping a clean look.</p>
  </article>

  <article class="page page--inverters">
    <div class="product" style="left:24px;top:34px;width:220px">
      <h2 class="product__title">Ferrand Hybrid</h2>
      <p class="product__body">The Vanta Hybrid is a flexible high voltage inverter ready for batteries now or later. It offers smart monitoring, wide voltage range and an extended warranty.</p>
    </div>
    <svg class="photo-tile" style="left:262px;top:40px" width="76" height="92" viewBox="0 0 76 92">
      <rect x="6" y="4" width="64" height="84" rx="5" fill="#e4e6e8" role="img" aria-label="Product shot of a hybrid inverter with red housing"/>
      <rect x="6" y="60" width="64" height="28" rx="5" fill="#d8282e"/>
    </svg>

    <div class="product" style="left:24px;top:150px;width:220px">
      <h2 class="product__title">Ferrand Orla 5.0-1 Inverter</h2>
      <p class="product__body">A great choice for larger homes or small business on a single phase supply. Fast to fit, with built in Wi-Fi and a wide power range from 3 to 8 kW.</p>
    </div>
    <svg class="photo-tile" style="left:262px;top:150px" width="76" height="92" viewBox="0 0 76 92">
      <rect x="6" y="4" width="64" height="84" rx="5" fill="#dcdfe2" role="img" aria-label="Product shot of a grey string inverter"/>
      <rect x="6" y="62" width="64" height="26" rx="5" fill="#4a4f55"/>
    </svg>

    <div class="ppa">
      <h2 class="product__title">PPA's</h2>
      <p class="product__body">A Power Purchase Agreement (PPA) gets you on the path to energy independence with no upfront costs.</p>
      <p class="product__body">A PPA is a fixed term plan through which you pay for electricity generated by an installed system for a fixed c/kWh rate.</p>
      <p class="product__body">Typically, the fixed c/kWh rate is lower than your current energy retailer charge and protects your business from rate rises during the term.</p>
    </div>

    <svg class="chart" viewBox="0 0 290 140" role="img" aria-label="Chart comparing a rising retailer rate with a flat PPA rate over twenty years">
      <line x1="20" y1="10" x2="20" y2="125" stroke="var(--rule)" stroke-width="1"/>
      <line x1="20" y1="125" x2="285" y2="125" stroke="var(--ink)" stroke-width=".8"/>
      <rect x="26" y="62" width="32" height="63" fill="#3a68b0"/>
      <g fill="#eef0f2" stroke="var(--rule)" stroke-width=".5">
        <rect x="60" y="62" width="225" height="63"/>
      </g>
      <g stroke="var(--rule)" stroke-width=".5">
        <line x1="80" y1="62" x2="80" y2="125"/><line x1="100" y1="62" x2="100" y2="125"/>
        <line x1="120" y1="62" x2="120" y2="125"/><line x1="140" y1="62" x2="140" y2="125"/>
        <line x1="160" y1="62" x2="160" y2="125"/><line x1="180" y1="62" x2="180" y2="125"/>
        <line x1="200" y1="62" x2="200" y2="125"/><line x1="220" y1="62" x2="220" y2="125"/>
        <line x1="240" y1="62" x2="240" y2="125"/><line x1="260" y1="62" x2="260" y2="125"/>
      </g>
      <line x1="20" y1="40" x2="285" y2="40" stroke="var(--teal)" stroke-width="1.5"/>
      <path d="M60 62 C 130 72, 210 98, 285 118" fill="none" stroke="var(--ink)" stroke-width="1.2" stroke-dasharray="3 2"/>
      <rect x="24" y="28" width="40" height="9" fill="var(--teal)"/>
      <text x="27" y="35" font-size="6" fill="#fff">Retailer rate</text>
      <text x="27" y="58" font-size="6" fill="var(--ink)">PPA rate</text>
      <text x="20" y="134" font-size="6" fill="var(--muted)">Year 1</text>
      <text x="262" y="134" font-size="6" fill="var(--muted)">Year 20</text>
    </svg>
  </article>
</section>

</body>
</html>
```